Grins of Maplecrest - Dental, needs a redesign

Purpose:
Redesign website: http://www.grinsofmaplecrest.example/

Sections are important, but for content, we can use existing website or have some placeholder text to fill in later.

Some of the required sections:
About us, contact us, services, our offices, our staff, patient education, patient forms (link to Molvaro can be used here), link to friendwall, testimonials

Editability:
We would like to be able to update and edit the content in the future, for small changes

Pictures:
Here is a link to the staff pictures we’d like to use on the website:
https://www.filecrate.example/sh/503k7pq2vv884x9/BBDPyrTe_wKQj7ZumfXKTgghb?dl=0
You don't have to use all the pictures; just a few.

Friendwall page:
https://www.friendwall.example/Grins-of-Maplecrest-527163048915276

Colors: Calming colors/images for a soothing feeling... to assure the patient that it'll not be that bad.

Target Market(s)

General population

Industry/Entity Type

Dental Clinic

Coding

Coded - Design and coding required

Number of Pages Required

5+ page

Requirements
Must have
• About us, contact us, services, our offices, our staff, patient education, patient forms (link to Molvaro can be used here), link to friendwall, testimonials.
• Just create the placeholders for content or use from existing website.
• The staff picture of everyone needs to be on the home page - because that makes it more personal and has received positive feedback from many patients.

```html
<!DOCTYPE html>
<html lang="en">
<head>
<meta charset="utf-8">
<title>Grins of Maplecrest - Dental</title>
<link rel="stylesheet" href="https://fonts.googleapis.com/css2?family=Roboto:wght@300;400;500;700&family=Great+Vibes&display=swap">
<style>
:root{
  --teal:#55c3cf;
  --teal-dark:#3fb3c0;
  --hero:#72e3f1;
  --purple:#b184e6;
  --ink:#444;
  --muted:#777;
  --field:#eeeff4;
  --line:#cfd6d9;
  --white:#fff;
  --map-blue:#4356a8;
  --map-land:#d9dbe3;
}
*{box-sizing:border-box;margin:0;padding:0}
html,body{width:1200px;height:3175px;overflow:hidden}
body{position:relative;background:var(--white);font-family:"Roboto",Arial,sans-serif;color:var(--ink)}
.abs{position:absolute}

/* navigation */
.site-nav{left:0;top:0;width:1200px;height:68px;background:var(--white)}
.brand{left:110px;top:14px;display:flex;align-items:center;gap:10px;font-size:15px;font-weight:500;color:var(--teal-dark)}
.brand-dot{width:34px;height:34px;border-radius:50%;background:#cfe9f3}
.menu{right:40px;top:24px;display:flex;gap:34px;list-style:none;font-size:12.5px;letter-spacing:.3px;color:#222}

/* hero */
.hero{left:0;top:68px;width:1200px;height:487px;background:var(--hero)}
.hero-photo{left:0;top:0;width:640px;height:487px;background:linear-gradient(90deg,#8a7a6e 0%,#c9b4a2 45%,rgba(114,227,241,0) 100%)}
.hero-title{left:430px;top:140px;width:600px;text-align:center;font-family:"Great Vibes",cursive;font-size:70px;color:var(--white)}
.hero-sub{left:430px;top:237px;width:600px;text-align:center;font-size:15px;color:var(--white)}
.btn-quote{left:624px;top:284px;width:117px;height:32px;background:var(--purple);color:var(--white);font-size:9px;font-weight:500;display:flex;align-items:center;justify-content:center;border-radius:2px}
.btn-surf{left:757px;top:284px;width:107px;height:32px;border:1px solid var(--white);color:var(--white);font-size:9px;font-weight:500;display:flex;align-items:center;justify-content:center;border-radius:2px}

/* stats */
.stat{width:320px;text-align:center}
.stat-label{font-size:17px;color:#333}
.stat-num{margin-top:14px;font-size:43px;font-weight:500;color:var(--teal)}

/* section headings */
.section-title{left:0;width:1200px;text-align:center;font-size:21px;font-weight:500;color:var(--teal)}
.dotted{left:50px;width:1100px;border-top:1px dashed var(--line)}

/* welcome */
.welcome{left:53px;top:745px;width:1090px;font-size:12.5px;line-height:1.6;color:var(--muted)}
.welcome p{margin-bottom:8px}
.dropcap{float:left;width:26px;height:26px;margin:2px 10px 0 0;background:var(--teal);color:var(--white);font-weight:700;display:flex;align-items:center;justify-content:center;font-size:14px}
.like-line{left:50px;top:908px;width:1100px;border-top:1px solid #e4e8ea}
.like-box{left:377px;top:886px;width:448px;height:44px;background:var(--white);border:1px solid #e0e4e6;border-radius:22px;display:flex;align-items:center;gap:10px;padding-left:120px;font-size:11px;color:#555}
.like-btn{background:#6d84b4;color:var(--white);font-size:10px;font-weight:700;padding:3px 8px;border-radius:2px}
.like-name{color:#5a73a8}

/* staff */
.staff-photo{left:0;top:948px;width:1200px;height:398px;background:linear-gradient(180deg,#7a5a44 0%,#5a4538 40%,#2d2a2c 100%)}

/* services */
.family-photo{left:95px;top:1439px;width:423px;height:444px;background:radial-gradient(ellipse at 50% 55%,#e7c7b2 0%,#c9a6a6 40%,#f3f3f6 75%,#fff 100%)}
.features{left:614px;top:1448px;list-style:none}
.features li{display:flex;align-items:center;height:56px;font-size:15.5px;color:#444}
.chev{width:22px;height:22px;margin-right:16px;background:#eef1f3;border-radius:3px;display:flex;align-items:center;justify-content:center}

/* new patient band */
.np-band{left:0;top:1896px;width:1200px;height:161px;background:var(--teal)}
.np-title{left:53px;top:50px;font-size:26px;font-weight:500;color:var(--white)}
.np-text{left:53px;top:90px;font-size:13.5px;color:#eafafc}
.np-btn{left:997px;top:72px;width:120px;height:44px;background:var(--white);color:var(--teal);font-size:12px;font-weight:500;display:flex;align-items:center;justify-content:center;border-radius:2px}

/* appointment form */
.select{left:78px;top:2131px;width:504px;height:42px;background:var(--teal);color:var(--white);font-size:11.5px;font-weight:500;display:flex;align-items:center;justify-content:space-between;padding:0 22px;border-radius:2px}
.label{font-size:12px;color:#444}
.field{background:var(--field);border-radius:2px}
.btn-timetable{left:396px;top:2376px;width:186px;height:45px;border:1px solid var(--teal);color:var(--teal);font-size:11.5px;font-weight:500;display:flex;align-items:center;justify-content:center;border-radius:2px}
.captcha{left:927px;top:2459px;font-size:12px;color:#555}
.captcha b{color:var(--teal);font-size:16px;font-weight:500}
.num{width:26px;height:26px;border-radius:50%;background:#e9f6f8;color:var(--teal);font-size:12px;display:flex;align-items:center;justify-content:center}
.btn-send{left:927px;top:2537px;width:190px;height:45px;background:var(--teal);color:var(--white);font-size:11.5px;font-weight:500;display:flex;align-items:center;justify-content:center;border-radius:2px}
.to-top{width:38px;height:38px;background:#c8cccf;display:flex;align-items:center;justify-content:center}

/* map + contact */
.map{left:0;top:2594px;width:1200px;height:470px;background:linear-gradient(120deg,var(--map-blue) 0%,#6d7cbd 22%,var(--map-land) 40%,var(--map-land) 62%,#6d7cbd 80%,var(--map-blue) 100%)}
.contact-card{left:470px;top:2630px;width:245px;height:290px;background:var(--white);text-align:center;padding-top:40px;font-size:12.5px;color:#555;line-height:1.65}
.contact-card h3{font-size:15px;font-weight:700;color:#333;margin-top:12px}
.contact-card h3:first-child{margin-top:0}
.hours-band{left:0;top:2979px;width:1200px;height:85px;background:rgba(86,200,214,.72);color:var(--white);font-size:21px;font-weight:500;display:flex;align-items:center;justify-content:center;letter-spacing:.3px}

/* footer */
.social{left:486px;top:3093px;display:flex;gap:19px}
.social span{width:31px;height:31px;border:1.5px solid #888;border-radius:50%}
.copyright{left:0;top:3138px;width:1200px;text-align:center;font-size:10px;color:#666}
</style>
</head>
<body>

<header class="site-nav abs">
  <div class="brand abs"><span class="brand-dot"></span>Grins of Maplecrest</div>
  <ul class="menu abs">
    <li>ABOUT US</li><li>SERVICES</li><li>OUR OFFICES</li><li>OUR STAFF</li><li>PATIENT EDUCATION</li><li>PATIENT FORMS</li><li>CONTACT</li>
  </ul>
</header>

<section class="hero abs">
  <div class="hero-photo abs" role="img" aria-label="Photo of a smiling patient cheering with clenched fists"></div>
  <h1 class="hero-title abs">Honestly Caring</h1>
  <p class="hero-sub abs">Quality Dentistry</p>
  <div class="btn-quote abs">REQUEST A QUOTE</div>
  <div class="btn-surf abs">GO ON SURFING</div>
</section>

<section>
  <div class="stat abs" style="left:64px;top:566px"><div class="stat-label">Years of experience</div><div class="stat-num">10 +</div></div>
  <div class="stat abs" style="left:439px;top:566px"><div class="stat-label">Patients a year</div><div class="stat-num">2480 +</div></div>
  <div class="stat abs" style="left:813px;top:566px"><div class="stat-label">People working</div><div class="stat-num">6 +</div></div>
</section>

<h2 class="section-title abs" style="top:688px">A Warm Welcome to You &amp; Your Family</h2>
<div class="dotted abs" style="top:722px"></div>
<div class="welcome abs">
  <p><span class="dropcap">D</span>Dr. Anika Solberg provides a full range of dental services to the whole family. Many of our patient families span multiple generations. Our Team are dedicated to taking the time needed to provide the very best care every patient deserves.</p>
  <p>Please tour our web site to learn more about family dentistry, cosmetic dentistry and our restorative dental services. We invite you to call us with any questions you may have - we all look forward to meeting you and your family!</p>
  <p>New patients looking for quality dental care in a relaxed environment are welcome! We accept PPO, Indeminity and Traditional insurance plans.</p>
</div>
<div class="like-line abs"></div>
<div class="like-box abs"><span class="like-btn">Like</span><span>You, <span class="like-name">Arben Kolari</span> and 4,886 others like this.</span></div>

<div class="staff-photo abs" role="img" aria-label="Group photo of the dental team seated together"></div>

<h2 class="section-title abs" style="top:1354px">We accept all PPO and indemnity insurance plans</h2>
<div class="dotted abs" style="top:1390px"></div>

<div class="family-photo abs" role="img" aria-label="Photo of a young family with two small children"></div>
<ul class="features abs">
  <li><span class="chev"><svg width="10" height="10" viewBox="0 0 10 10"><path d="M2 3.5l3 3 3-3" fill="none" stroke="#9aa4a8" stroke-width="1.4"/></svg></span>Saturday &amp; Tuesday late appointments</li>
  <li><span class="chev"><svg width="10" height="10" viewBox="0 0 10 10"><path d="M2 3.5l3 3 3-3" fill="none" stroke="#9aa4a8" stroke-width="1.4"/></svg></span>Kid friendly environment</li>
  <li><span class="chev"><svg width="10" height="10" viewBox="0 0 10 10"><path d="M2 3.5l3 3 3-3" fill="none" stroke="#9aa4a8" stroke-width="1.4"/></svg></span>State of the art digital X-ray</li>
  <li><span class="chev"><svg width="10" height="10" viewBox="0 0 10 10"><path d="M2 3.5l3 3 3-3" fill="none" stroke="#9aa4a8" stroke-width="1.4"/></svg></span>Emergencies welcome</li>
  <li><span class="chev"><svg width="10" height="10" viewBox="0 0 10 10"><path d="M2 3.5l3 3 3-3" fill="none" stroke="#9aa4a8" stroke-width="1.4"/></svg></span>Preventive, restorative &amp; cosmetic dentistry</li>
  <li><span class="chev"><svg width="10" height="10" viewBox="0 0 10 10"><path d="M2 3.5l3 3 3-3" fill="none" stroke="#9aa4a8" stroke-width="1.4"/></svg></span>Root canal treatment</li>
  <li><span class="chev"><svg width="10" height="10" viewBox="0 0 10 10"><path d="M2 3.5l3 3 3-3" fill="none" stroke="#9aa4a8" stroke-width="1.4"/></svg></span>Extractions</li>
  <li><span class="chev"><svg width="10" height="10" viewBox="0 0 10 10"><path d="M2 3.5l3 3 3-3" fill="none" stroke="#9aa4a8" stroke-width="1.4"/></svg></span>Dentures</li>
</ul>

<section class="np-band abs">
  <h2 class="np-title abs">New Patient Form</h2>
  <p class="np-text abs">If you are a new patient, you may find it convenient to fill out the New Patient Forms online before you visit us.</p>
  <div class="np-btn abs">HIRE US NOW</div>
</section>

<h2 class="section-title abs" style="top:2067px">MAKE AN APPOITMENT</h2>
<div class="dotted abs" style="top:2099px"></div>

<form>
  <div class="select abs">- CHOOSE DEPARTMENT -<svg width="18" height="12" viewBox="0 0 18 12"><path d="M2 3l7 6 7-6" fill="none" stroke="#fff" stroke-width="2"/></svg></div>

  <div class="label abs" style="left:91px;top:2190px">First Name *</div>
  <div class="field abs" style="left:78px;top:2213px;width:504px;height:43px"></div>
  <div class="label abs" style="left:625px;top:2190px">Last Name</div>
  <div class="field abs" style="left:612px;top:2213px;width:505px;height:43px"></div>

  <div class="label abs" style="left:91px;top:2272px">Phone</div>
  <div class="field abs" style="left:78px;top:2296px;width:504px;height:42px"></div>
  <div class="label abs" style="left:625px;top:2272px">E-mail *</div>
  <div class="field abs" style="left:612px;top:2296px;width:505px;height:42px"></div>

  <div class="label abs" style="left:91px;top:2354px">Appointment Date (mm/dd/yyyy)</div>
  <div class="field abs" style="left:78px;top:2376px;width:292px;height:45px"></div>
  <div class="btn-timetable abs">VIEW TIMETABLE</div>
  <div class="label abs" style="left:625px;top:2354px">Social Security Number</div>
  <div class="field abs" style="left:612px;top:2376px;width:505px;height:45px"></div>

  <div class="label abs" style="left:91px;top:2437px">Your Message *</div>
  <div class="field abs" style="left:78px;top:2459px;width:825px;height:127px"></div>

  <div class="captcha abs">Please select number: <b>three</b></div>
  <div class="num abs" style="left:929px;top:2489px">1</div>
  <div class="num abs" style="left:969px;top:2489px">2</div>
  <div class="num abs" style="left:1009px;top:2489px">3</div>
  <div class="num abs" style="left:1049px;top:2489px">4</div>
  <div class="num abs" style="left:1089px;top:2489px">5</div>
  <div class="btn-send abs">SEND MESSAGE</div>
</form>
<div class="to-top abs" style="left:1130px;top:2496px"><svg width="16" height="10" viewBox="0 0 16 10"><path d="M2 8l6-6 6 6" fill="none" stroke="#fff" stroke-width="1.6"/></svg></div>

<section>
  <div class="map abs" role="img" aria-label="Street map of the clinic neighbourhood"></div>
  <address class="contact-card abs" style="font-style:normal">
    <h3>ADDRESS</h3>
    <p>Nuvola Health Center<br>18 Linden Row, Maplecrest,<br>MA 02190</p>
    <h3>EMAIL</h3>
    <p>info@grinsofmaplecrest.example</p>
    <h3>PHONE</h3>
    <p>1-555-014-2290</p>
  </address>
  <div class="hours-band abs">24 HOURS A DAY, 7 DAYS A WEEK, 365 DAYS A YEAR FOR YOU</div>
</section>

<footer>
  <div class="social abs"><span></span><span></span><span></span><span></span><span></span></div>
  <p class="copyright abs">Lumen©2015. All rights reserved</p>
  <div class="to-top abs" style="left:1130px;top:3086px"><svg width="16" height="10" viewBox="0 0 16 10"><path d="M2 8l6-6 6 6" fill="none" stroke="#fff" stroke-width="1.6"/></svg></div>
</footer>

</body>
</html>
```